Signage for a Utility vehicle and Trailer for our modern residential Building company in NZ

We need a design for signage to go onto our Utility Vehicle (Ute - Kestrel Dunmore 2008 GVS with canopy as pictured) and trailer (in picture). Both vehicles are silver and our logo is Orange and dark Grey/Black. We also require the TQW logo and Approved Framers Logo. We would want to stick with the Orange and charcoal grey or black colours throughout the design. We are looking for something with a modern, classy feel as our main market is architectural homes and renovations. We would like to convey a professional yet personable business with a modern, edgy feel to it. Our phone number needs to be clear and easily readable. Preferably there needs to be a space available to add our website address at a later date once we have one!!
Updates

Project Deadline Extended
Reason: Having a busy week - need more time to respond to designs and request some changes. Probably 5 days was an unrealistic deadline. Thanks

Target Market(s)

People wanting to build high-spec architectural homes

Industry/Entity Type

Residential Construction

Font styles to use
Sans Serif

Colors
f37122
333333
000000
474747

Requirements
Must have
• TQW logo and Approved Framers Logo
• phone number 027 384951
• New builds - Renovations - Extensions
• Builders of Exceptional Homes.
• Building your dream home? We can help you make it a reality.
Nice to have
• Possibly cool/edgy graphic - sketch of house or house plans

```html
<!DOCTYPE html>
<html lang="en">
<head>
<meta charset="utf-8">
<title>Ashcombe Building Contractors – Vehicle Signage</title>
<link rel="stylesheet" href="https://fonts.googleapis.com/css2?family=Montserrat:wght@400;600;800;900&display=swap">
<style>
  :root{
    --orange:#f37122;
    --orange-deep:#e0610f;
    --charcoal:#333333;
    --black:#000000;
    --grey:#474747;
    --white:#ffffff;
    --bg:#e6e7e8;
  }
  *{box-sizing:border-box;margin:0;padding:0}
  html,body{width:1200px;height:944px;overflow:hidden}
  body{background:var(--bg);font-family:"Montserrat",sans-serif;position:relative}
  .panel{position:absolute;overflow:hidden;background:var(--white);box-shadow:0 2px 10px rgba(0,0,0,.15)}
  .panel svg.art{position:absolute;inset:0;width:100%;height:100%}
  .abs{position:absolute}

  .brand{display:flex;align-items:center;gap:10px;color:var(--charcoal);font-weight:400;letter-spacing:.04em;text-transform:uppercase;line-height:1.1}
  .brand-mark{border:3px solid var(--charcoal);flex:none}

  .badge{border-radius:50%;background:var(--grey);border:4px solid var(--white);box-shadow:0 0 0 2px var(--charcoal)}

  .phone-line{display:flex;align-items:center;gap:14px;color:var(--white);font-weight:800;white-space:nowrap}
  .call-us{color:var(--orange);font-weight:800;line-height:.95;text-transform:uppercase;letter-spacing:.08em}

  /* Ute side wrap */
  .ute{left:30px;top:30px;width:1140px;height:390px}
  .ute .brand{left:420px;top:120px;font-size:20px}
  .ute .brand-mark{width:46px;height:46px}
  .ute .services{left:395px;top:196px;font-size:19px;font-weight:800;color:var(--orange);letter-spacing:.02em}
  .ute .services b{color:var(--black)}
  .ute .badge{left:50px;top:90px;width:100px;height:100px}
  .ute .phone-line{left:360px;top:244px;font-size:38px;letter-spacing:.08em}
  .ute .call-us{font-size:16px}

  /* Trailer side */
  .side{left:30px;top:460px;width:640px;height:330px}
  .side .brand{left:26px;top:28px;font-size:12px}
  .side .brand-mark{width:30px;height:30px}
  .side .headline{right:26px;top:26px;text-align:right;font-size:30px;font-weight:900;line-height:1.08;text-transform:uppercase}
  .side .headline .w{color:var(--white)}
  .side .headline .k{color:var(--black)}
  .side .phone-line{left:26px;top:226px;font-size:40px;gap:12px;transform:rotate(-8deg);transform-origin:left center}
  .side .call-us{font-size:16px}
  .side .badge{right:24px;top:170px;width:78px;height:78px}

  /* Trailer rear */
  .rear{left:710px;top:460px;width:460px;height:330px}
  .rear .brand{left:110px;top:22px;font-size:17px}
  .rear .brand-mark{width:44px;height:44px}
  .rear .badge{left:195px;top:98px;width:70px;height:70px}
  .rear .services{left:0;right:0;top:182px;text-align:center;color:var(--white);font-size:25px;font-weight:900;line-height:1.05;text-transform:uppercase}
  .rear .phone-line{left:22px;top:270px;font-size:40px;letter-spacing:.06em}
  .rear .call-us{font-size:16px}
</style>
</head>
<body>

<section class="panel ute" aria-label="Ute side wrap">
  <svg class="art" viewBox="0 0 1140 390" preserveAspectRatio="none" aria-hidden="true">
    <rect x="0" y="52" width="1140" height="4" fill="var(--orange)"/>
    <polygon points="0,300 1140,300 1140,390 0,390" fill="var(--orange)"/>
    <polygon points="330,232 1140,232 1140,310 290,310" fill="var(--black)"/>
    <polygon points="0,290 260,290 240,310 0,310" fill="var(--black)"/>
    <polygon points="860,60 1140,60 1140,232 930,232 880,170" fill="var(--grey)"/>
    <polygon points="930,60 1040,60 990,150" fill="var(--charcoal)"/>
  </svg>
  <div class="badge abs" role="img" aria-label="Practitioner badge"></div>
  <div class="brand abs"><span class="brand-mark"></span><span>Ashcombe<br>Building<br>Contractors Ltd</span></div>
  <div class="services abs">NEW BUILDS <b>- RENOVATIONS -</b> EXTENSIONS</div>
  <div class="phone-line abs"><span class="call-us">Call<br>us!</span><span>027 384951</span></div>
</section>

<section class="panel side" aria-label="Trailer side panel">
  <svg class="art" viewBox="0 0 640 330" preserveAspectRatio="none" aria-hidden="true">
    <polygon points="0,150 640,0 640,170 0,250" fill="var(--orange)"/>
    <polygon points="330,0 640,0 640,60 250,150" fill="var(--orange-deep)" opacity=".5"/>
    <polygon points="0,200 560,130 640,130 640,250 0,300" fill="var(--black)"/>
    <polygon points="0,300 640,250 640,262 0,312" fill="var(--orange)"/>
  </svg>
  <div class="brand abs"><span class="brand-mark"></span><span>Ashcombe<br>Building<br>Contractors Ltd</span></div>
  <div class="headline abs"><span class="w">Builders of</span><br><span class="k">Exceptional</span><br><span class="w">Homes</span></div>
  <div class="phone-line abs"><span class="call-us">Call<br>us!</span><span>027 384951</span></div>
  <div class="badge abs" role="img" aria-label="Practitioner badge"></div>
</section>

<section class="panel rear" aria-label="Trailer rear panel">
  <svg class="art" viewBox="0 0 460 330" preserveAspectRatio="none" aria-hidden="true">
    <polygon points="0,80 230,125 460,40 460,330 0,330" fill="var(--orange)"/>
    <polygon points="260,118 460,46 460,56 270,126" fill="var(--white)"/>
    <rect x="0" y="262" width="460" height="56" fill="var(--black)"/>
  </svg>
  <div class="brand abs"><span class="brand-mark"></span><span>Ashcombe<br>Building<br>Contractors Ltd</span></div>
  <div class="badge abs" role="img" aria-label="Practitioner badge"></div>
  <div class="services abs">New Builds<br>Renovations<br>Extensions</div>
  <div class="phone-line abs"><span class="call-us">Call<br>us!</span><span>027 384951</span></div>
</section>

</body>
</html>
```